Business Card Design Project

Looking for a logo and business card for a Real State Business i will be opening. The name is not choosen yet , but will probably be RTV IMOVEIS.
I was thinking black and silver colors, but am open to nice ideas.
I did add a business card that i liked a lot, am looking for something like that, with logo in black or silver in a black card. The logo i was thinking in the letters RTV as i uploaded or something or little and cute buildings or a house...just ideas, can be any nice logo.
Updates

You guys can add other colors if you want, I like colors very "BRIGHT" and "open", like red, pink, strong colors. almost glow in the dark colors. lol

Designers,

I've increased more 88 dollars in the budget for 1st place cause I will want envelope designs... small and big sizes.

So 1st place is now U$248,00. 

No need to send the envelope designs right now... only the business cards designs.

Thank you.

Industry/Entity Type

Business

Requirements
Must have
• Renata Tavares Vilela

www.RTVimoveis-exemplo.com.br

+554188316402

renata@rtvimoveis-exemplo.com.br

```html
<!DOCTYPE html>
<html lang="pt-BR">
<head>
<meta charset="utf-8">
<title>RTV Imoveis – Cartão de visita</title>
<link rel="stylesheet" href="https://fonts.googleapis.com/css2?family=Questrial&display=swap">
<style>
  :root {
    --stage: #000000;
    --card: #ffffff;
    --ink: #111111;
    --accent: #ff6699;
    --rule: #b5b5b5;
  }
  * { margin: 0; padding: 0; box-sizing: border-box; }
  html, body {
    width: 1200px;
    height: 1000px;
    overflow: hidden;
    position: relative;
    background: var(--stage);
    font-family: "Questrial", "Helvetica Neue", Arial, sans-serif;
  }
  .card {
    position: absolute;
    left: 48px;
    top: 200px;
    width: 1104px;
    height: 600px;
    overflow: hidden;
    background: var(--card);
  }
  .brand-mark {
    position: absolute;
    left: 191px;
    top: 110px;
    width: 250px;
    height: 250px;
    background: var(--accent);
  }
  .brand {
    position: absolute;
    left: 22px;
    top: 412px;
    width: 590px;
    text-align: center;
    font-size: 90px;
    line-height: 1;
    letter-spacing: 1px;
    color: var(--ink);
    font-weight: 400;
    white-space: nowrap;
  }
  .divider {
    position: absolute;
    left: 660px;
    top: 22px;
    width: 8px;
    height: 558px;
    background: repeating-linear-gradient(to bottom, var(--rule) 0 1px, transparent 1px 3px);
  }
  .contact {
    position: absolute;
    left: 717px;
    top: 231px;
    width: 375px;
    font-size: 23px;
    line-height: 35px;
    font-style: normal;
    color: var(--ink);
    white-space: nowrap;
  }
  .contact .name,
  .contact .web,
  .contact .at { color: var(--accent); }
</style>
</head>
<body>
  <main class="card">
    <div class="brand-mark" role="img" aria-label="Marca RTV Imoveis"></div>
    <div class="brand">RTV IMOVEIS</div>
    <div class="divider"></div>
    <address class="contact">
      <div class="name">Renata Tavares Vilela</div>
      <div class="phone">+554188316402</div>
      <div class="web">www.RTVimoveis-exemplo.com.br</div>
      <div class="email">renata<span class="at">@</span>rtvimoveis-exemplo.com.br</div>
    </address>
  </main>
</body>
</html>
```